Mechanical Engineering Business needs a Label Design for Bottle.

We need a Label design for 2 Bottle Sizes of Cutting Paste. This is used for Machine Work Shops big and small to do applications for different cutting processes. Example : Tapping / Broaching / Drilling / Reaming / Knurling / etc. An example of a similar product can be found at https://drellix-goo.com/product/16-oz-drellix-goo-bottle/ ... https://drellix-goo.com/product/2-oz-drellix-goo-bottle/ ... Our product will be named Vorn - Gel or Vorning - Gel with our Company logo attached. Currently, we are open to ideas and do not have any fixed concept.

```html
<!DOCTYPE html>
<html lang="en">
<head>
<meta charset="utf-8">
<title>Vorn-Gel Machining Lubricant Label</title>
<link rel="stylesheet" href="https://fonts.googleapis.com/css2?family=Barlow:wght@300;400;500;600;700;800&display=swap">
<style>
  :root {
    --maroon: #7f1435;
    --black: #0c0c0d;
    --white: #ffffff;
    --page: #ececec;
  }
  * { margin: 0; padding: 0; box-sizing: border-box; }
  html, body {
    width: 1200px;
    height: 1034px;
    overflow: hidden;
    background: var(--page);
    font-family: "Barlow", Arial, sans-serif;
  }
  .label {
    position: absolute;
    left: 394px;
    top: 37px;
    width: 412px;
    height: 960px;
    background: var(--white);
    box-shadow: 4px 6px 10px rgba(0,0,0,0.25);
    overflow: hidden;
  }
  .label__shapes {
    position: absolute;
    inset: 0;
    width: 100%;
    height: 100%;
  }
  .line {
    position: absolute;
    left: 0;
    right: 0;
    text-align: center;
    transform: translateY(-50%);
    line-height: 1;
    white-space: nowrap;
  }
  .brand {
    top: 166px;
    display: flex;
    justify-content: center;
    align-items: center;
    gap: 10px;
    color: var(--white);
    font-size: 30px;
    font-weight: 500;
    letter-spacing: 1px;
  }
  .brand__dot {
    width: 22px;
    height: 22px;
    border-radius: 50%;
    background: var(--maroon);
  }
  .category {
    color: var(--white);
    font-size: 32px;
    font-weight: 700;
  }
  .category--one { top: 264px; }
  .category--two { top: 306px; }
  .product-name {
    top: 452px;
    color: var(--maroon);
    font-size: 70px;
    letter-spacing: -1px;
  }
  .product-name__bold { font-weight: 800; }
  .product-name__light { font-weight: 300; }
  .grade {
    position: absolute;
    left: 81px;
    top: 494px;
    width: 248px;
    height: 44px;
    border: 2px solid var(--maroon);
    border-radius: 18px 4px 18px 4px;
    color: var(--maroon);
    font-size: 22px;
    font-weight: 600;
    display: flex;
    align-items: center;
    justify-content: center;
  }
  .formula {
    top: 683px;
    color: var(--white);
    font-size: 40px;
    font-weight: 800;
  }
  .uses {
    color: var(--white);
    font-size: 21px;
    font-weight: 500;
  }
  .uses--one { top: 729px; }
  .uses--two { top: 756px; }
  .uses--three { top: 785px; }
  .shake {
    top: 872px;
    color: var(--white);
    font-size: 32px;
    font-weight: 700;
  }
  .net-weight {
    top: 905px;
    color: var(--white);
    font-size: 20px;
    font-weight: 500;
  }
</style>
</head>
<body>
  <main class="label">
    <svg class="label__shapes" viewBox="0 0 433 1008" preserveAspectRatio="none" aria-hidden="true">
      <defs>
        <linearGradient id="panelTone" x1="0" y1="0" x2="1" y2="1">
          <stop offset="0" stop-color="#1c1c1e"/>
          <stop offset="1" stop-color="#0a0a0b"/>
        </linearGradient>
      </defs>
      <polygon points="0,0 433,0 433,352 216.5,416 0,352" fill="var(--maroon)"/>
      <polygon points="0,0 433,0 433,348 216.5,388 0,348" fill="url(#panelTone)"/>
      <polygon points="0,648 216.5,590 433,648 433,1008 0,1008" fill="var(--maroon)"/>
      <polygon points="0,660 216.5,618 433,660 433,825 216.5,880 0,825" fill="url(#panelTone)"/>
    </svg>

    <div class="line brand"><span class="brand__dot"></span><span class="brand__name">ARKWELL TOOLS</span></div>

    <div class="line category category--one">MACHINING</div>
    <div class="line category category--two">LUBRICANT</div>

    <div class="line product-name"><span class="product-name__bold">VORN</span><span class="product-name__light">-GEL</span></div>
    <div class="grade">Professional Grade</div>

    <div class="line formula">THICK FORMULA</div>
    <div class="line uses uses--one">• TAPPING • BROACHING</div>
    <div class="line uses uses--two">• DRILLING • REAMING</div>
    <div class="line uses uses--three">• KNURLING</div>

    <div class="line shake">SHAKE WELL</div>
    <div class="line net-weight">NET WT.16-OZ</div>
  </main>
</body>
</html>
```